Business card design needed

I need a business card for my new Food & Lifestyle Coaching business - "Bloomvale Food & Lifestlye Coaching"

i already have a logo and would like to have that incorporated into the business card, obviously.

i would like a design that says "fresh" and "funky" - my target market is female, aged 20-45 so i want something that will stand out to them when they see it.

My "Company Colour" is Apple Green
Updates

Thankyou to everyone who has submitted a design for my project. At this stage i have quite a large number of designs to chose from and with only a short time until my project closes i am focusing now on chosing from those i have already shortlisted so am unfortunately not considering any new desings.

Thankyou again for your interest in my project.

Target Market(s)

Female, Health Conscious (or looking to improve their health/lifestyle), aged between 20-45

Industry/Entity Type

Business

Contact Information for Business Card

Tamsin Corley
Ph: 0417382946
Email: eatwell@marovex.com

Requirements
Must have
• Must include my existing Logo
Nice to have
• Would be nice to incoirporate and appointment card on the back

```html
<!DOCTYPE html>
<html lang="en">
<head>
<meta charset="utf-8">
<title>Bloomvale Food &amp; Lifestlye Coaching – Business Card</title>
<link rel="stylesheet" href="https://fonts.googleapis.com/css2?family=Crimson+Pro:wght@500&display=swap">
<style>
  :root {
    --apple-green: #a3e24a;
    --card-pink-centre: #f26e85;
    --card-pink-edge: #ee6aa2;
    --ink: #2a2226;
    --serif: "Crimson Pro", Georgia, serif;
  }
  * { margin: 0; padding: 0; box-sizing: border-box; }
  html, body {
    width: 1200px;
    height: 900px;
    overflow: hidden;
  }
  body {
    position: relative;
    background: var(--apple-green);
    font-family: var(--serif);
    color: var(--ink);
  }
  .card {
    position: absolute;
    width: 665px;
    height: 410px;
    overflow: hidden;
    background: radial-gradient(ellipse at 50% 50%, var(--card-pink-centre) 0%, var(--card-pink-edge) 100%);
  }
  .card--contact { left: 128px; top: 40px; }
  .card--brand { left: 470px; top: 470px; }

  .brand-mark {
    position: absolute;
    display: flex;
    align-items: center;
    gap: 10px;
    font-weight: 500;
    color: var(--ink);
    white-space: nowrap;
  }
  .brand-mark__dot {
    flex: none;
    border-radius: 50%;
    background: var(--apple-green);
  }
  .brand-mark__text { display: flex; flex-direction: column; line-height: 1; }

  .card--contact .brand-mark { left: 12px; top: 18px; }
  .card--contact .brand-mark__dot { width: 40px; height: 40px; }
  .card--contact .brand-mark__name { font-size: 50px; }
  .card--contact .brand-mark__tagline { font-size: 14px; margin-top: 4px; }

  .card--brand .brand-mark { left: 120px; top: 140px; gap: 16px; }
  .card--brand .brand-mark__dot { width: 72px; height: 72px; }
  .card--brand .brand-mark__name { font-size: 84px; }
  .card--brand .brand-mark__tagline { font-size: 22px; margin-top: 8px; }

  .holder-name {
    position: absolute;
    left: 120px;
    top: 166px;
    font-size: 44px;
    letter-spacing: 3px;
    font-weight: 500;
    white-space: nowrap;
  }
  .contact-list {
    position: absolute;
    left: 142px;
    top: 225px;
    list-style: none;
    font-size: 19px;
    letter-spacing: 1.5px;
    white-space: nowrap;
  }
  .contact-list li {
    display: flex;
    align-items: center;
    gap: 10px;
    height: 36px;
  }
  .contact-list svg { flex: none; }
</style>
</head>
<body>

  <section class="card card--contact" aria-label="Business card, contact side">
    <div class="brand-mark">
      <span class="brand-mark__dot"></span>
      <span class="brand-mark__text">
        <span class="brand-mark__name">Bloomvale</span>
        <span class="brand-mark__tagline">Food &amp; Lifestlye Coaching</span>
      </span>
    </div>

    <h1 class="holder-name">Tamsin Corley</h1>

    <ul class="contact-list">
      <li>
        <svg width="34" height="20" viewBox="0 0 34 20" aria-hidden="true">
          <rect x="1" y="1" width="32" height="18" fill="none" stroke="#2a2226" stroke-width="1.6"/>
          <path d="M1 1 L17 12 L33 1 M1 19 L13 9 M33 19 L21 9" fill="none" stroke="#2a2226" stroke-width="1.6"/>
        </svg>
        <span>eatwell@marovex.com</span>
      </li>
      <li>
        <svg width="24" height="26" viewBox="0 0 24 26" aria-hidden="true">
          <path d="M7 2 C4 3 3 6 3 9 C3 16 9 23 15 24 C18 24.5 20 23 21 21 L17 17 C16 18 14.5 18.5 13.5 17.5 C11 15 9.5 12.5 9 10 C9 9 10 8 11 7.5 L9 2 Z" fill="#2a2226"/>
        </svg>
        <span>0417382946</span>
      </li>
    </ul>
  </section>

  <section class="card card--brand" aria-label="Business card, brand side">
    <div class="brand-mark">
      <span class="brand-mark__dot"></span>
      <span class="brand-mark__text">
        <span class="brand-mark__name">Bloomvale</span>
        <span class="brand-mark__tagline">Food &amp; Lifestlye Coaching</span>
      </span>
    </div>
  </section>

</body>
</html>
```